Flooring Company Stationery Design Project

I need Business card, presentation folder, letterhead and envelope design.
I want the design to show a lot of creativity and that it has a modern look but still professional.
The company has a retail store but we specialize in in-home shopping.

Design must have a "flooring" company style. Creativity is going to be the main thing we'll be looking for. We want something that will stand out of the competition.

We are a remodeling busines and we want to look like one but with a good look.

PLEASE USE FOLLOWING LINK FOR ANY PHOTOS NEEDED
http://www.velmorick.com/syndicate/logos/choose_brands.html
Updates

PLEASE USE ANY PHOTOS NEEDED FROM HERE

Target Market(s)

Our target customer are 35-50 years old and decision makers are usually women

Industry/Entity Type

Retail

Requirements
Must have
• Color red
PHOTOS NEEDED CAN BE USED FROM HERE

```html
<!DOCTYPE html>
<html lang="en">
<head>
<meta charset="utf-8">
<title>Hearthline Stationery</title>
<link rel="stylesheet" href="https://fonts.googleapis.com/css2?family=Open+Sans:wght@400;700&family=Arimo&display=swap">
<style>
  :root {
    --bg: #dde1e2;
    --paper: #ffffff;
    --red: #d2101c;
    --red-deep: #a3000e;
    --red-bright: #e8000f;
    --orange: #fcaa00;
    --ink: #1b1b1b;
    --shadow: 0 2px 6px rgba(0,0,0,.35);
  }
  * { margin: 0; padding: 0; box-sizing: border-box; }
  html, body { width: 1200px; height: 1000px; overflow: hidden; }
  body { background: var(--bg); font-family: "Open Sans", Arial, sans-serif; position: relative; }

  .sheet { position: absolute; background: var(--paper); box-shadow: var(--shadow); overflow: hidden; }
  .piece-label { position: absolute; font-family: "Arimo", Arial, sans-serif; font-size: 19px; letter-spacing: 1.5px; color: var(--ink); }

  .company-name { position: absolute; font-weight: 700; color: var(--red); line-height: 1; }

  .band { position: absolute; left: 0; bottom: 0; display: block; }

  .contact { position: absolute; color: #fff; line-height: 1.45; }
  .contact b { color: var(--orange); font-weight: 700; }
  .contact .sep { padding: 0 8px; }

  /* Letterhead */
  .letterhead { left: 38px; top: 33px; width: 703px; height: 910px; }
  .letterhead .company-name { left: 42px; top: 84px; font-size: 44px; }
  .letterhead .contact { right: 41px; top: 818px; font-size: 13.5px; text-align: right; }
  .letterhead .site { position: absolute; left: 44px; top: 786px; color: var(--red); font-weight: 700; font-size: 14px; }

  /* Envelope */
  .envelope { left: 467px; top: 128px; width: 700px; height: 383px; border-radius: 12px 12px 0 0; }
  .envelope .flap { position: absolute; left: 0; top: 0; width: 700px; height: 77px; background: linear-gradient(180deg, var(--red-bright), var(--red-deep)); }
  .envelope .flap-text { position: absolute; left: 0; right: 0; top: 8px; transform: rotate(180deg); text-align: center; color: #fff; font-size: 10.5px; line-height: 1.45; }
  .envelope .flap-text .flap-site { font-size: 13px; font-weight: 700; }
  .envelope .flap-text b { color: var(--orange); }
  .envelope .company-name { left: 23px; top: 126px; font-size: 42px; }

  /* Cards */
  .card { left: 772px; width: 361px; height: 225px; border-radius: 10px; }
  .card-front { top: 455px; }
  .card-front .company-name { left: 21px; top: 40px; font-size: 36px; }
  .card-front .holder { position: absolute; right: 24px; top: 191px; color: #fff; font-weight: 700; font-size: 12px; }
  .card-back { top: 720px; background: radial-gradient(ellipse at 70% 30%, var(--red-bright) 40%, var(--red-deep) 100%); }
  .card-back .site { position: absolute; left: 0; right: 0; top: 60px; text-align: center; color: #fff; font-weight: 700; font-size: 16px; }
  .card-back .contact { left: 0; right: 0; top: 107px; text-align: center; font-size: 12.5px; }
</style>
</head>
<body>

<section class="sheet letterhead">
  <span class="company-name">Hearthline</span>
  <svg class="band" width="703" height="140" viewBox="0 0 703 140" aria-hidden="true">
    <path d="M0 100 C220 48 470 14 703 0" fill="none" stroke="var(--orange)" stroke-width="6"/>
    <path d="M0 140 L0 124 C210 70 460 34 703 20 L703 140 Z" fill="var(--red-deep)"/>
  </svg>
  <span class="site">www.hearthline.com</span>
  <p class="contact">
    <b>e:</b> info@hearthline.com<br>
    <b>a:</b> Harbor Mill Blvd. Suit C, Tampa, FL 33601<br>
    <b>t:</b> (813) 555-01426<span class="sep">I</span><b>f:</b> (813) 555-0188
  </p>
</section>
<span class="piece-label" style="left:42px;top:953px">Letterhead</span>

<section class="sheet envelope">
  <div class="flap">
    <p class="flap-text">
      <span class="flap-site">www.hearthline.com</span><br>
      <b>E:</b> info@hearthline.com &nbsp;I&nbsp; <b>A:</b> Harbor Mill Blvd. Suit C, Tampa, FL 33601<br>
      <b>T:</b> (813) 555-01426 &nbsp;I&nbsp; <b>F:</b> (813) 555-0188
    </p>
  </div>
  <span class="company-name">Hearthline</span>
</section>
<span class="piece-label" style="left:472px;top:519px">Envelope</span>

<section class="sheet card card-front">
  <span class="company-name">Hearthline</span>
  <svg class="band" width="361" height="92" viewBox="0 0 361 92" aria-hidden="true">
    <path d="M0 66 C110 36 240 12 361 2" fill="none" stroke="var(--orange)" stroke-width="4"/>
    <path d="M0 92 L0 84 C110 52 240 26 361 14 L361 92 Z" fill="var(--red-deep)"/>
  </svg>
  <span class="holder">Name Name Name</span>
</section>
<span class="piece-label" style="left:778px;top:689px">Business Card Front</span>

<section class="sheet card card-back">
  <p class="site">www.hearthline.com</p>
  <p class="contact">
    <b>E:</b> info@hearthline.com<br>
    <b>A:</b> Harbor Mill Blvd. Suit C, Tampa, FL 33601<br>
    <b>T:</b> (813) 555-01426<span class="sep">I</span><b>F:</b> (813) 555-0188
  </p>
</section>
<span class="piece-label" style="left:778px;top:951px">Business Card Back</span>

</body>
</html>
```